Melbourne Locksmith Needs a Web Site

We need a web site for our new Locksmith business in Melbourne Australia. Our business is called " Corbett Row Locksmiths" . (Corbett row is a well known in the city and has the famous railway station , it is a main icon of melbourne . Maybe we could incorperate the station maybe in the front page or heading background. our services include Automotive Locksmithing ( Cuting keys to cars, opening cars etc / Master Keys Systems/ Commercial work / Domestic . Also we have no logo yet. but we can get that in the future if needed.

Target Market(s)

(Automotive ) Lost keys to cars, Trucks, Jammed Ignitions, Opening Vehicles. mobile locksmith in a van, Locked out of your house ?

Industry/Entity Type

Business

Number of Pages Required

4 page

Font styles to use
Sans Serif

Colors

Designer to choose colors to be used in the design.

Requirements
Must have
• Phone number easy to read on web site.
Nice to have
• map of where we are, show case pictures of common lock problems for automotive eg ( damaged keys/ Broken).

```html
<!DOCTYPE html>
<html lang="en">
<head>
<meta charset="utf-8">
<title>Corbett Row Locksmiths</title>
<link rel="stylesheet" href="https://fonts.googleapis.com/css2?family=Aldrich&family=Open+Sans:wght@400;600;700&display=swap">
<style>
:root{
  --red:#e03232;
  --blue:#0f4c96;
  --ink:#1a1a1a;
  --text:#333;
  --grey-bg:#ededed;
  --line:#c9c9c9;
  --white:#fff;
  --black:#050505;
  --foot-text:#e6e6e6;
}
*{box-sizing:border-box;margin:0;padding:0}
html,body{width:1200px;height:2857px;overflow:hidden;background:var(--white)}
body{position:relative;font-family:"Open Sans",Arial,sans-serif;color:var(--text)}
.abs{position:absolute}

/* header */
.topbar{left:585px;top:0;width:615px;height:53px;background:var(--blue);clip-path:polygon(20px 0,100% 0,100% 100%,0 100%);display:flex;align-items:center;gap:40px;padding-left:45px;color:var(--white);font-size:17px;font-weight:600}
.topbar .item{display:flex;align-items:center;gap:12px}
.topbar .ico{width:30px;height:30px;border-radius:50%;background:var(--red);display:flex;align-items:center;justify-content:center}
.brand{left:99px;top:18px;display:flex;align-items:center;gap:12px}
.brand .dot{width:40px;height:40px;border-radius:50%;background:var(--red)}
.brand .name{font-family:"Aldrich",sans-serif;font-size:25px;line-height:1.1;color:var(--blue);letter-spacing:2px;text-transform:uppercase}
.nav{top:90px;left:440px;display:flex;font-family:"Open Sans",Arial,sans-serif;font-size:15.5px;color:var(--ink);text-transform:uppercase}
.nav a{color:inherit;text-decoration:none;padding:0 32px;border-left:1px solid var(--line)}
.nav a:first-child{border-left:0}
.nav a.current{color:var(--red)}

/* hero */
.hero{left:0;top:128px;width:1200px;height:543px;background:
  radial-gradient(ellipse 180px 220px at 230px 230px,#d9b8a4 0%,#c59a85 45%,rgba(197,154,133,0) 100%),
  radial-gradient(ellipse 320px 300px at 170px 520px,#151515 0%,#1d1d1d 60%,rgba(29,29,29,0) 100%),
  radial-gradient(ellipse 260px 200px at 200px 40px,#4d6b3a 0%,rgba(77,107,58,0) 100%),
  radial-gradient(ellipse 220px 260px at 480px 150px,#a49b92 0%,rgba(164,155,146,0) 100%),
  linear-gradient(100deg,#3f4e36 0%,#7d7b72 32%,#b9bcbd 52%,#e4e7e9 70%,#aab0b5 85%,#7e858b 100%)}
.hero-caption{left:0;top:583px;width:1200px;height:88px;background:rgba(60,60,60,.75);color:var(--white);text-align:center;font-family:"Aldrich",sans-serif;font-size:25px;line-height:30px;padding-top:14px;letter-spacing:.3px}
.hero-arrow{top:603px}

/* about */
.section-title{font-family:"Aldrich",sans-serif;font-size:33px;font-weight:400;text-transform:uppercase;color:var(--red)}
.section-title .blue{color:var(--blue)}
.about-title{left:99px;top:720px}
.about-rule{left:99px;top:776px;width:644px;height:2px;background:var(--line)}
.about-lead{left:99px;top:801px;width:644px;font-size:15.5px;font-weight:700;color:var(--ink)}
.about-body{left:99px;top:830px;width:644px;font-size:12.4px;line-height:23.5px;color:var(--text)}
.btn{background:var(--red);color:var(--white);font-size:15.5px;text-transform:uppercase;display:flex;align-items:center;justify-content:center;gap:8px}
.about-btn{left:99px;top:995px;width:154px;height:42px}

.inquiry{left:800px;top:726px;width:301px;height:303px;background:#f3f3f3;border:1px solid #d6d6d6}
.inquiry-head{height:51px;background:var(--blue);color:var(--white);font-family:"Aldrich",sans-serif;font-size:20px;display:flex;align-items:center;justify-content:center;border-radius:6px 6px 0 0;margin:-1px -1px 0}
.field{position:absolute;left:16px;width:268px;height:34px;background:var(--white);border:1px solid #dcdcdc;font-size:12px;color:#aaa;display:flex;align-items:center;gap:8px;padding-left:12px}
.field.msg{height:65px;align-items:flex-start;padding-top:10px}
.inquiry-btn{left:884px;top:995px;width:134px;height:41px}

/* services */
.services{left:0;top:1118px;width:1200px;height:501px;background:var(--grey-bg)}
.center-title{left:0;width:1200px;text-align:center}
.title-rule{left:410px;width:380px;height:2px;background:var(--line)}
.card{top:1273px;width:238px;height:203px;border:3px solid var(--blue);box-shadow:0 8px 10px -4px rgba(0,0,0,.45)}
.card.active{border-color:var(--red)}
.card.keys{background:radial-gradient(ellipse 90px 70px at 70px 40px,#c9a58e,rgba(201,165,142,0)),radial-gradient(ellipse 110px 90px at 150px 120px,#5b5f66,rgba(91,95,102,0)),linear-gradient(150deg,#3b3d40,#9a9ca0 55%,#cfd1d3)}
.card.opening{background:radial-gradient(ellipse 90px 60px at 70px 45px,#c49b82,rgba(196,155,130,0)),radial-gradient(ellipse 120px 100px at 170px 90px,#111,rgba(17,17,17,0)),linear-gradient(160deg,#e8eaec,#7d8187 55%,#2a2b2e)}
.card.master{background:radial-gradient(ellipse 110px 60px at 110px 100px,#c8c9cb,rgba(200,201,203,0)),linear-gradient(160deg,#f6f6f6,#dcdcdc 50%,#b7b8ba)}
.card.commercial{background:radial-gradient(ellipse 80px 70px at 140px 90px,#3a3a3a,rgba(58,58,58,0)),radial-gradient(ellipse 70px 60px at 50px 60px,#c39a82,rgba(195,154,130,0)),linear-gradient(160deg,#d9dbdd,#9c9fa3 60%,#6c6f73)}
.card .badge{position:absolute;left:50%;bottom:-3px;transform:translateX(-50%);width:84px;height:44px;border-radius:42px 42px 0 0;background:var(--blue);display:flex;align-items:center;justify-content:center}
.card.active .badge{background:var(--red)}
.card-label{top:1502px;width:238px;text-align:center;font-family:"Aldrich",sans-serif;font-size:17px;color:var(--blue);text-transform:uppercase}
.card-label.active{color:var(--red)}
.toggle{top:1537px;width:26px;height:26px;background:var(--blue);color:var(--white);font-size:22px;line-height:25px;text-align:center;font-weight:700}
.toggle.active{background:var(--red)}

/* call to action */
.cta-text{left:130px;top:1660px;width:940px;text-align:center;font-size:16px;line-height:26px;color:var(--ink)}
.cta-btn{left:510px;top:1739px;width:180px;height:42px}

/* gallery */
.gallery{left:0;top:1825px;width:1200px;height:728px;background:var(--grey-bg)}
.tile.drill{background:radial-gradient(ellipse 120px 90px at 330px 120px,#c79a80,rgba(199,154,128,0)),radial-gradient(ellipse 140px 90px at 380px 40px,#3f6fb3,rgba(63,111,179,0)),linear-gradient(120deg,#30363d,#6d7b88 40%,#b8c1c9 70%,#2c3e5c)}
.tile.fob{background:radial-gradient(ellipse 90px 70px at 80px 100px,#1e1e1e,rgba(30,30,30,0)),radial-gradient(ellipse 100px 80px at 80px 40px,#e2b8a3,rgba(226,184,163,0)),linear-gradient(135deg,#f1ece8,#cfc7c0 60%,#9c928a)}
.tile.handle{background:radial-gradient(ellipse 90px 70px at 140px 90px,#c89c83,rgba(200,156,131,0)),linear-gradient(150deg,#8d9096,#c5c8cc 45%,#b89a6b 80%,#8f7a55)}
.tile.door{background:radial-gradient(ellipse 70px 130px at 70px 170px,#1f2024,rgba(31,32,36,0)),radial-gradient(ellipse 60px 40px at 150px 270px,#e0c21a,rgba(224,194,26,0)),linear-gradient(90deg,#d8cfbe,#b69c6a 55%,#e9e2d4)}
.tile.knob{background:radial-gradient(ellipse 70px 50px at 160px 90px,#c9a13a,rgba(201,161,58,0)),radial-gradient(ellipse 80px 50px at 70px 80px,#d2a48b,rgba(210,164,139,0)),linear-gradient(150deg,#e8e4de,#b9b0a5 60%,#7a6f63)}
.tile.pick{background:radial-gradient(ellipse 120px 90px at 110px 110px,#c99c82,rgba(201,156,130,0)),linear-gradient(150deg,#f3f3f3,#c8cacc 50%,#8f9399)}
.tile.fit{background:radial-gradient(ellipse 90px 110px at 160px 120px,#3d4c7a,rgba(61,76,122,0)),radial-gradient(ellipse 50px 40px at 140px 70px,#b88a6e,rgba(184,138,110,0)),linear-gradient(90deg,#8a7552,#c9a877 45%,#a48a5e)}

/* footer */
.footer{left:0;top:2553px;width:1200px;height:257px;background:var(--black)}
.foot-head{font-weight:600;font-size:14.5px;text-transform:uppercase;color:var(--white)}
.foot-rule{height:2px;background:#555}
.foot-links{list-style:none;font-size:13px;line-height:28.5px;color:var(--foot-text)}
.foot-links li::before{content:"›";color:var(--red);margin-right:8px}
.contact-col{color:var(--foot-text)}
.contact-row{display:flex;gap:14px;font-size:12.5px;line-height:19px;align-items:flex-start}
.contact-row b{color:var(--white)}
.contact-row .ico{width:16px;flex:none;display:flex;justify-content:center;padding-top:2px}
.map{left:587px;top:2636px;width:226px;height:133px;border:2px solid #ddd;background:radial-gradient(circle at 90px 70px,#e15b4c 0 5px,rgba(0,0,0,0) 6px),linear-gradient(135deg,#9fc1e3,#e6e8d2 40%,#f1ead6 60%,#93b9de)}
.foot-brand{left:897px;top:2640px;width:205px;display:flex;flex-direction:column;align-items:center;gap:14px}
.foot-brand .dot{width:40px;height:40px;border-radius:50%;background:#9a9a9a}
.foot-brand .name{font-family:"Aldrich",sans-serif;font-size:20px;color:#cfcfcf;letter-spacing:2px;text-transform:uppercase;text-align:center;line-height:1.25}
.copybar{left:0;top:2810px;width:1200px;height:47px;background:var(--blue);color:var(--white);font-size:12.5px;display:flex;align-items:center;padding-left:99px}
.social{top:2821px;width:26px;height:26px;background:var(--red)}
</style>
</head>
<body>

<div class="abs topbar">
  <div class="item"><span class="ico"><svg width="14" height="14" viewBox="0 0 24 24"><path fill="#fff" d="M6.6 10.8a15 15 0 0 0 6.6 6.6l2.2-2.2c.3-.3.7-.4 1-.2 1.1.4 2.3.6 3.6.6.6 0 1 .4 1 1V20c0 .6-.4 1-1 1A17 17 0 0 1 3 4c0-.6.4-1 1-1h3.5c.6 0 1 .4 1 1 0 1.3.2 2.5.6 3.6.1.3 0 .7-.2 1z"/></svg></span>123-456-7890</div>
  <div class="item"><span class="ico"><svg width="14" height="12" viewBox="0 0 24 18"><rect x="1" y="1" width="22" height="16" rx="2" fill="none" stroke="#fff" stroke-width="2"/><path d="M1 2l11 8 11-8" fill="none" stroke="#fff" stroke-width="2"/></svg></span>info@corbettrowlocksmiths.au</div>
</div>

<div class="abs brand">
  <span class="dot"></span>
  <span class="name">Corbett Row<br>Locksmiths</span>
</div>

<nav class="abs nav">
  <a class="current" href="#">Home</a>
  <a href="#">About Us</a>
  <a href="#">Services</a>
  <a href="#">Gallery</a>
  <a href="#">Contact Us</a>
</nav>

<div class="abs hero" role="img" aria-label="Photo of a locksmith opening a car door lock"></div>
<div class="abs hero-caption">At Corbett Row Locksmiths, We Know What It Takes To Keep Your<br>Home &amp; Business Safe &amp; Secure</div>
<svg class="abs hero-arrow" style="left:58px" width="24" height="46" viewBox="0 0 24 46"><path d="M14 2L3 23l11 21M22 2L11 23l11 21" fill="none" stroke="#fff" stroke-width="2"/></svg>
<svg class="abs hero-arrow" style="left:1118px" width="24" height="46" viewBox="0 0 24 46"><path d="M10 2l11 21-11 21M2 2l11 21L2 44" fill="none" stroke="#fff" stroke-width="2"/></svg>

<h2 class="abs section-title about-title">About Corbett Row <span class="blue">Locksmiths</span></h2>
<div class="abs about-rule"></div>
<p class="abs about-lead">Lorem ipsum dolor sit amet, consectetuer adipiscing elit, sed diam nonummy</p>
<p class="abs about-body">Lorem ipsum dolor sit amet, consectetuer adipiscing elit, sed diam nonummy nibh euismod tincidunt ut laoreet dolore magna aliquam erat volutpat. Ut wisi enim ad minim veniam, quis nostrud exerci tation ullamcorper suscipit lobortis nisl ut aliquip ex ea commodo consequat. Duis autem vel eum iriure dolor in hendrerit in vulputate velit esse molestie consequat, vel illum dolore eu feugiat nulla facilisis at vero eros et accumsan et iusto odio dignissim qui blandit praesent luptatum zzril delenit augue duis dolore te feugait nulla facilisi. Lorem ipsum dolor sit amet, consectetuer adipiscing elit.</p>
<div class="abs btn about-btn">Read More <svg width="8" height="10" viewBox="0 0 8 10"><path d="M0 0l8 5-8 5z" fill="#fff"/></svg></div>

<div class="abs inquiry">
  <div class="inquiry-head">QUICK INQUIRY</div>
  <div class="field" style="top:61px"><svg width="11" height="12" viewBox="0 0 12 12"><circle cx="6" cy="3.5" r="3" fill="#bbb"/><path d="M0 12c0-4 3-5 6-5s6 1 6 5z" fill="#bbb"/></svg>Your Name</div>
  <div class="field" style="top:103px"><svg width="11" height="11" viewBox="0 0 24 24"><path fill="#bbb" d="M6.6 10.8a15 15 0 0 0 6.6 6.6l2.2-2.2c.3-.3.7-.4 1-.2 1.1.4 2.3.6 3.6.6.6 0 1 .4 1 1V20c0 .6-.4 1-1 1A17 17 0 0 1 3 4c0-.6.4-1 1-1h3.5c.6 0 1 .4 1 1 0 1.3.2 2.5.6 3.6.1.3 0 .7-.2 1z"/></svg>Phone</div>
  <div class="field" style="top:145px"><svg width="12" height="9" viewBox="0 0 24 18"><rect x="1" y="1" width="22" height="16" fill="none" stroke="#bbb" stroke-width="2"/><path d="M1 2l11 8 11-8" fill="none" stroke="#bbb" stroke-width="2"/></svg>Email</div>
  <div class="field msg" style="top:187px"><svg width="12" height="11" viewBox="0 0 12 11"><path d="M0 0h12v8H4l-3 3V8H0z" fill="#bbb"/></svg>Message</div>
</div>
<div class="abs btn inquiry-btn">Submit <svg width="8" height="10" viewBox="0 0 8 10"><path d="M0 0l8 5-8 5z" fill="#fff"/></svg></div>

<div class="abs services"></div>
<h2 class="abs section-title center-title" style="top:1168px">Our <span class="blue">Services</span></h2>
<div class="abs title-rule" style="top:1226px"></div>

<div class="abs card keys active" style="left:99px" role="img" aria-label="Photo of a key cutting machine in use">
  <span class="badge"><svg width="30" height="22" viewBox="0 0 30 22"><path d="M4 10l4-8h14l4 8h2v8h-3v3h-4v-3H9v3H5v-3H2v-8z" fill="#fff"/><circle cx="8" cy="13" r="2" fill="#e03232"/><circle cx="22" cy="13" r="2" fill="#e03232"/></svg></span>
</div>
<div class="abs card opening" style="left:354px" role="img" aria-label="Photo of a car door being opened with a tool">
  <span class="badge"><svg width="26" height="26" viewBox="0 0 26 26"><circle cx="19" cy="7" r="5" fill="none" stroke="#fff" stroke-width="3"/><path d="M15 11L3 23M6 20l3 3M9 17l3 3" stroke="#fff" stroke-width="3"/></svg></span>
</div>
<div class="abs card master" style="left:608px" role="img" aria-label="Photo of a lock cylinder with keys">
  <span class="badge"><svg width="28" height="22" viewBox="0 0 28 22"><rect x="2" y="6" width="24" height="15" rx="2" fill="#fff"/><path d="M10 6V3h8v3" fill="none" stroke="#fff" stroke-width="2.5"/><rect x="12" y="11" width="4" height="4" fill="#0f4c96"/></svg></span>
</div>
<div class="abs card commercial" style="left:863px" role="img" aria-label="Photo of a hand turning a key in a commercial lock">
  <span class="badge"><svg width="26" height="24" viewBox="0 0 26 24"><rect x="3" y="6" width="8" height="18" fill="#fff"/><rect x="13" y="0" width="10" height="24" fill="#fff"/><rect x="15" y="3" width="2" height="2" fill="#0f4c96"/><rect x="19" y="3" width="2" height="2" fill="#0f4c96"/><rect x="15" y="8" width="2" height="2" fill="#0f4c96"/><rect x="19" y="8" width="2" height="2" fill="#0f4c96"/></svg></span>
</div>

<div class="abs card-label active" style="left:99px">Cutting Keys to Cars</div>
<div class="abs card-label" style="left:354px">Opening Cars</div>
<div class="abs card-label" style="left:608px">Master Keys Systems</div>
<div class="abs card-label" style="left:863px">Commercial Work</div>
<div class="abs toggle active" style="left:205px">−</div>
<div class="abs toggle" style="left:460px">+</div>
<div class="abs toggle" style="left:714px">+</div>
<div class="abs toggle" style="left:969px">+</div>

<p class="abs cta-text">Lorem ipsum dolor sit amet, consectetuer adipiscing elit, sed diam nonummy nibh euismod tincidunt ut laoreet dolore magna aliquam erat volutpat. Ut wisi enim ad minim veniam, quis nostrud exerci tation ullamcorper suscipit.</p>
<div class="abs btn cta-btn">Call Us Today <svg width="8" height="10" viewBox="0 0 8 10"><path d="M0 0l8 5-8 5z" fill="#fff"/></svg></div>

<div class="abs gallery"></div>
<h2 class="abs section-title center-title" style="top:1884px">Lock Problem <span class="blue">Solved Gallery</span></h2>
<div class="abs title-rule" style="top:1941px;left:280px;width:640px"></div>

<div class="abs tile drill" style="left:99px;top:1985px;width:467px;height:244px" role="img" aria-label="Photo of a locksmith drilling a door lock"></div>
<div class="abs tile fob" style="left:99px;top:2252px;width:219px;height:234px" role="img" aria-label="Photo of a hand holding a car key fob"></div>
<div class="abs tile handle" style="left:347px;top:2252px;width:219px;height:234px" role="img" aria-label="Photo of a door handle being repaired"></div>
<div class="abs tile door" style="left:592px;top:1985px;width:233px;height:314px" role="img" aria-label="Photo of a locksmith working at a front door with a toolbox"></div>
<div class="abs tile knob" style="left:592px;top:2326px;width:233px;height:160px" role="img" aria-label="Photo of a key entering a brass door knob"></div>
<div class="abs tile pick" style="left:855px;top:1985px;width:246px;height:244px" role="img" aria-label="Photo of hands picking a car door lock"></div>
<div class="abs tile fit" style="left:855px;top:2250px;width:246px;height:236px" role="img" aria-label="Photo of a locksmith fitting a door lock"></div>

<footer class="abs footer"></footer>
<div class="abs foot-head" style="left:99px;top:2585px">Quick Links</div>
<div class="abs foot-rule" style="left:99px;top:2614px;width:165px"></div>
<ul class="abs foot-links" style="left:99px;top:2627px">
  <li>Home</li><li>About Us</li><li>Services</li><li>Gallery</li><li>Contact</li>
</ul>

<div class="abs foot-head" style="left:293px;top:2585px">Contact Details</div>
<div class="abs foot-rule" style="left:293px;top:2614px;width:195px"></div>
<div class="abs contact-col" style="left:293px;top:2630px;display:flex;flex-direction:column;gap:12px">
  <div class="contact-row"><span class="ico"><svg width="12" height="16" viewBox="0 0 12 16"><path d="M6 0a6 6 0 0 1 6 6c0 4-6 10-6 10S0 10 0 6a6 6 0 0 1 6-6z" fill="#e03232"/><circle cx="6" cy="6" r="2.2" fill="#050505"/></svg></span><span><b>Corbett Row Locksmiths</b><br>123 Pg Duis Aute Irur Dolore<br>Srephenderit Amit In Voluptate</span></div>
  <div class="contact-row"><span class="ico"><svg width="13" height="13" viewBox="0 0 24 24"><path fill="#e03232" d="M6.6 10.8a15 15 0 0 0 6.6 6.6l2.2-2.2c.3-.3.7-.4 1-.2 1.1.4 2.3.6 3.6.6.6 0 1 .4 1 1V20c0 .6-.4 1-1 1A17 17 0 0 1 3 4c0-.6.4-1 1-1h3.5c.6 0 1 .4 1 1 0 1.3.2 2.5.6 3.6.1.3 0 .7-.2 1z"/></svg></span><span>+ (123) 456 7890</span></div>
  <div class="contact-row"><span class="ico"><svg width="14" height="12" viewBox="0 0 14 12"><rect x="1" y="1" width="12" height="10" rx="1" fill="#e03232"/><rect x="3" y="3" width="8" height="2" fill="#050505"/></svg></span><span>+ (123) 456 7890</span></div>
  <div class="contact-row"><span class="ico"><svg width="14" height="10" viewBox="0 0 24 18"><rect x="0" y="0" width="24" height="18" rx="2" fill="#e03232"/><path d="M1 2l11 8 11-8" fill="none" stroke="#050505" stroke-width="2"/></svg></span><span>info@corbettrowlocksmiths.com</span></div>
</div>

<div class="abs foot-head" style="left:587px;top:2585px">Location Map</div>
<div class="abs foot-rule" style="left:587px;top:2614px;width:135px"></div>
<div class="abs map" role="img" aria-label="Map showing the business location in the city"></div>

<div class="abs foot-brand">
  <span class="dot"></span>
  <span class="name">Corbett Row<br>Locksmiths</span>
</div>

<div class="abs copybar">Copyright © 2017 Corbett Row Locksmiths. All Rights Reserved</div>
<div class="abs social" style="left:966px"></div>
<div class="abs social" style="left:1003px"></div>
<div class="abs social" style="left:1040px"></div>
<div class="abs social" style="left:1077px"></div>

</body>
</html>
```